Valtoria - Managed Service Provider Brochure

Our company has launched a new division, a "Managed Service Provider (MSP)" division and we are looking for a new bifold brochure to market our company.
This new service provides our clients a vendor management solution to save money and control their procurement process. We would like to maintain the same color scheme of black and red as the core colors along our logo.
We have provided a recent powerpoint presentation done by our team containing the copy material that can be used for this project. We do not require the images stay the same so feel free to incorporate what works best in the design.
Thank you.
It Company

```html
<!DOCTYPE html>
<html lang="en">
<head>
<meta charset="utf-8">
<title>Valtoria – Managed Service Provider Brochure</title>
<link rel="stylesheet" href="https://fonts.googleapis.com/css2?family=Lato:wght@400;700&family=Montserrat:wght@400;500&family=Roboto:wght@400&display=swap">
<style>
:root{
  --red:#c9232b;
  --red-deep:#a91c23;
  --black:#231f20;
  --ink:#2b2b2b;
  --paper:#ffffff;
  --paper-grey:#eeeeee;
  --backdrop:#5a4330;
  --photo-warm:#c9a98c;
  --photo-cool:#b9c3cc;
}
*{margin:0;padding:0;box-sizing:border-box}
html,body{width:1200px;height:907px;overflow:hidden;background:var(--backdrop)}
body{position:relative;font-family:"Lato",Arial,sans-serif;color:var(--ink)}
.spread{position:absolute;left:80px;top:88px;width:1010px;height:717px;background:var(--paper);overflow:hidden;box-shadow:0 6px 18px rgba(0,0,0,.35)}
.spread-art{position:absolute;left:0;top:0;width:1010px;height:717px}
.page-left-fade{position:absolute;left:0;top:0;width:505px;height:717px;background:linear-gradient(90deg,var(--paper) 0%,var(--paper-grey) 100%)}
.hero-faded{position:absolute;left:0;top:0;width:505px;height:250px;background:linear-gradient(180deg,#d9d9d9 0%,#ececec 60%,rgba(255,255,255,0) 100%)}
.section-title{position:absolute;left:0;height:27px;width:212px}
.section-title span{position:absolute;left:20px;top:3px;font-family:"Montserrat",Arial,sans-serif;font-size:17px;color:#fff;font-weight:500}
.about-title{top:175px}
.values-title{top:374px}
.about-text{position:absolute;left:18px;top:214px;width:452px;font-size:10.8px;line-height:12.5px;text-align:justify;color:var(--ink)}
.about-text p+p{margin-top:3px}
.values-list{position:absolute;left:18px;top:413px;list-style:none;font-size:11.3px;color:var(--ink)}
.values-list li{height:21.5px;padding-left:14px;position:relative}
.values-list li::before{content:"";position:absolute;left:0;top:2px;width:5px;height:5px;border-right:2.5px solid var(--red);border-bottom:2.5px solid var(--red);transform:rotate(-45deg)}
.brand-small{position:absolute;left:20px;top:502px;font-size:32px;font-weight:400;color:var(--black);letter-spacing:.5px;line-height:1}
.tagline-small{position:absolute;left:21px;top:542px;font-size:8px;color:var(--ink)}
.contact{position:absolute;left:20px;top:573px;list-style:none;font-size:11.3px;line-height:14.5px;color:var(--ink)}
.contact li{position:relative;padding-left:13px;margin-bottom:6px}
.contact li::before{content:"";position:absolute;left:0;top:4px;width:6px;height:6px;background:var(--red);border-radius:50%}
.phone-in-hand{position:absolute;left:300px;top:537px;width:72px;height:180px;border-radius:10px 10px 30px 30px;background:linear-gradient(180deg,#2c3a4a 0%,#2f6fb0 45%,#e3b99a 80%,#f0cbb0 100%)}
.meeting-photo{position:absolute;left:505px;top:200px;width:505px;height:247px;background:linear-gradient(90deg,var(--photo-cool) 0%,#e6ddd5 35%,var(--photo-warm) 60%,#d6c7b9 80%,#8c4a3c 100%)}
.brand{position:absolute;left:560px;top:44px;font-size:58px;font-weight:400;color:var(--black);letter-spacing:1px;line-height:1}
.tagline{position:absolute;left:562px;top:118px;font-size:14px;color:var(--ink);letter-spacing:.3px}
.program{position:absolute;right:25px;top:523px;font-family:"Montserrat",Arial,sans-serif;font-size:21px;color:#fff}
.product{position:absolute;right:25px;top:552px;font-family:"Roboto",Arial,sans-serif;font-size:44px;color:#fff;line-height:1.1}
.web{position:absolute;right:28px;top:638px;font-size:16px;letter-spacing:4.4px;color:#fff}
</style>
</head>
<body>
<main class="spread">
  <div class="page-left-fade"></div>
  <div class="hero-faded" role="img" aria-label="Soft, faded portrait photo of a smiling woman"></div>
  <div class="meeting-photo" role="img" aria-label="Photo of colleagues in a friendly office meeting around a laptop"></div>

  <svg class="spread-art" viewBox="0 0 1010 717" aria-hidden="true">
    <polygon points="842,197 1010,14 1010,197" fill="var(--black)"/>
    <line x1="832" y1="199" x2="1010" y2="4" stroke="var(--red)" stroke-width="5"/>
    <rect x="505" y="195" width="332" height="4" fill="var(--red)"/>
    <polygon points="622,447 1010,447 1010,717 398,717" fill="var(--red)"/>
    <polygon points="800,662 1010,662 1010,717 740,717" fill="var(--red-deep)" opacity=".5"/>
    <rect x="505" y="447" width="113" height="5" fill="var(--red)"/>
    <polygon points="608,447 620,447 395,717 383,717" fill="var(--black)"/>
    <polygon points="440,630 1010,630 1010,662 413,662" fill="var(--black)"/>
    <g class="about-bar">
      <polygon points="0,175 182,175 170,202 0,202" fill="var(--red)"/>
      <polygon points="185,175 197,175 185,202 173,202" fill="var(--red)"/>
      <polygon points="199,175 211,175 199,202 187,202" fill="var(--red)"/>
    </g>
    <g class="values-bar">
      <polygon points="0,374 222,374 210,401 0,401" fill="var(--red)"/>
      <polygon points="225,374 237,374 225,401 213,401" fill="var(--red)"/>
      <polygon points="239,374 251,374 239,401 227,401" fill="var(--red)"/>
      <polygon points="253,374 265,374 253,401 241,401" fill="var(--red)"/>
    </g>
  </svg>

  <div class="section-title about-title"><span>About us</span></div>
  <div class="about-text">
    <p>Valtoria National Staffing works to unite the best talent with the best employment across a national and geographical scope. We have established ourselves as industry leaders by working to place ourselves at the forefront of the Managed Service Provider and Vendor Management System approach to staffing.</p>
    <p>At Valtoria National Staffing we have found that success can be measured by the strength of the relationships that we cultivate with both our candidates and clients. We have extended this principle toward the relationships that we sustain with MSP and VMS providers as well. We work closely with MSP program managers to formulate strong relationships built upon trust and accomplishment that will in turn benefit our clients.</p>
  </div>

  <div class="section-title values-title"><span>Our Core Values</span></div>
  <ul class="values-list">
    <li>Operate with the utmost integrity to ensure that all relationships are built on trust</li>
    <li>Communicate in a straightforward and transparent manner</li>
    <li>Build a reputation that will serve as a positive reflection on our clients and candidates</li>
  </ul>

  <div class="brand-small">Valtoria</div>
  <div class="tagline-small">Talent and trust, delivered.</div>
  <ul class="contact">
    <li>2240 Harbor Line Ave<br>Suite 310<br>Brookfield, PA 19480</li>
    <li>1-855-55-TEAMS (1-855-558-3267)</li>
    <li>info@valtoriastaff.com</li>
    <li>www.valtoriastaff.com</li>
  </ul>
  <div class="phone-in-hand" role="img" aria-label="Illustration of a hand holding a smartphone showing a login screen"></div>

  <div class="brand">Valtoria</div>
  <div class="tagline">Talent and trust, delivered.</div>
  <div class="program">Management Service Program</div>
  <div class="product">VMS Technology</div>
  <div class="web">www.valtoriastaff.com</div>
</main>
</body>
</html>
```